K/Loft Coffee Cup Christmas Design

2023 Christmas Design for our 12oz Coffee Cup, we are a coffee roaster wholesaler, so these go out to all or wholesale customers for them to use at Xmas, Christmas/Coffee themed, we are based in New Zealand, so Summertime.....must include our logo

```html
<!DOCTYPE html>
<html lang="en">
<head>
<meta charset="utf-8">
<title>K/Loft Coffee Cup – 2023 Christmas Summertime</title>
<link rel="stylesheet" href="https://fonts.googleapis.com/css2?family=Oswald:wght@200;400;500&family=Dancing+Script:wght@600&family=Montserrat:wght@400&display=swap">
<style>
  :root {
    --page: #ffffff;
    --gold-top: #ffc52a;
    --gold-upper: #f1bf5e;
    --gold-mid: #d8a443;
    --gold-bottom: #b8832e;
    --ink-light: #ffffff;
    --doodle-tint: #fff1d6;
  }
  html, body {
    margin: 0;
    padding: 0;
    width: 1200px;
    height: 1126px;
    overflow: hidden;
    background: var(--page);
  }
  .canvas {
    position: relative;
    width: 1200px;
    height: 1126px;
  }
  .cup-wrap {
    position: absolute;
    left: 47px;
    top: 271px;
    width: 1105px;
    height: 583px;
  }
  .brand-name {
    font-family: "Oswald", sans-serif;
    font-weight: 400;
    fill: var(--ink-light);
  }
  .year {
    font-family: "Oswald", sans-serif;
    font-weight: 200;
    fill: var(--ink-light);
  }
  .headline {
    font-family: "Oswald", sans-serif;
    font-weight: 500;
    fill: var(--ink-light);
  }
  .script {
    font-family: "Dancing Script", cursive;
    font-weight: 600;
    fill: var(--ink-light);
  }
  .size-mark {
    font-family: "Montserrat", sans-serif;
    font-weight: 400;
    fill: var(--ink-light);
  }
  .doodle-spot {
    fill: url(#doodle-glow);
  }
</style>
</head>
<body>
<main class="canvas">
  <svg class="cup-wrap" viewBox="258 55 1473 777" xmlns="http://www.w3.org/2000/svg" aria-labelledby="cup-title">
    <title id="cup-title">12oz cup wrap: 2023 Christmas Summertime</title>
    <defs>
      <linearGradient id="wrap-fill" x1="0" y1="55" x2="0" y2="832" gradientUnits="userSpaceOnUse">
        <stop offset="0" stop-color="var(--gold-top)"/>
        <stop offset="0.32" stop-color="var(--gold-upper)"/>
        <stop offset="0.68" stop-color="var(--gold-mid)"/>
        <stop offset="1" stop-color="var(--gold-bottom)"/>
      </linearGradient>
      <radialGradient id="doodle-glow">
        <stop offset="0" stop-color="var(--doodle-tint)" stop-opacity="0.28"/>
        <stop offset="1" stop-color="var(--doodle-tint)" stop-opacity="0"/>
      </radialGradient>
      <radialGradient id="tree-glow">
        <stop offset="0" stop-color="var(--doodle-tint)" stop-opacity="0.32"/>
        <stop offset="1" stop-color="var(--doodle-tint)" stop-opacity="0"/>
      </radialGradient>
      <clipPath id="wrap-clip">
        <path d="M258 198 Q995 -88 1731 198 L1481 832 Q995 638 509 832 Z"/>
      </clipPath>
    </defs>

    <path class="cup-dieline"
          d="M258 198 Q995 -88 1731 198 L1481 832 Q995 638 509 832 Z"
          fill="url(#wrap-fill)"/>

    <g class="doodle-pattern" clip-path="url(#wrap-clip)" role="img"
       aria-label="Faint scattered Christmas doodles: snowflakes, stars, bows, baubles, bells, candy canes, trees and a snowman">
      <ellipse class="doodle-spot" cx="450" cy="335" rx="80" ry="70"/>
      <ellipse class="doodle-spot" cx="465" cy="500" rx="70" ry="55"/>
      <ellipse class="doodle-spot" cx="715" cy="360" rx="60" ry="45"/>
      <ellipse class="doodle-spot" cx="690" cy="520" rx="75" ry="80"/>
      <ellipse class="doodle-spot" cx="560" cy="650" rx="70" ry="70"/>
      <ellipse class="doodle-spot" cx="660" cy="735" rx="70" ry="55"/>
      <ellipse class="doodle-spot" cx="855" cy="318" rx="45" ry="40"/>
      <ellipse class="doodle-spot" cx="1170" cy="340" rx="70" ry="60"/>
      <ellipse class="doodle-spot" cx="1375" cy="405" rx="50" ry="55"/>
      <ellipse class="doodle-spot" cx="1270" cy="490" rx="65" ry="60"/>
      <ellipse class="doodle-spot" cx="1550" cy="450" rx="90" ry="95"/>
      <ellipse class="doodle-spot" cx="1330" cy="615" rx="60" ry="60"/>
      <ellipse class="doodle-spot" cx="1475" cy="725" rx="55" ry="45"/>
      <ellipse class="doodle-spot" cx="860" cy="665" rx="45" ry="40"/>
      <ellipse class="doodle-spot" cx="1135" cy="660" rx="45" ry="35"/>
    </g>

    <text class="brand-name" x="995" y="232" text-anchor="middle" font-size="52">K/Loft Coffee Co.</text>

    <ellipse class="tree-outline" role="img"
             aria-label="White line drawing of a Christmas tree with a bauble hanging from its tip, framing the title"
             cx="995" cy="380" rx="130" ry="78"
             fill="url(#tree-glow)"/>

    <text class="year" x="996" y="482" text-anchor="middle" font-size="74">2023</text>
    <text class="headline" x="1000" y="548" text-anchor="middle" font-size="80"
          textLength="296" lengthAdjust="spacingAndGlyphs">CHRISTMAS</text>
    <text class="script" x="995" y="612" text-anchor="middle" font-size="84"
          textLength="366" lengthAdjust="spacingAndGlyphs">Summertime</text>

    <text class="size-mark" x="995" y="691" text-anchor="middle" font-size="23">12oz</text>
  </svg>
</main>
</body>
</html>
```